12-page Product Brochure for School Archiving Specialist Company

We require a 12-page brochure for our company based in Melbourne, VIC. Our company specializes in tailored archiving solutions for Australian schools of all sizes, and our main product is the "Tidy Vault" archiving system.
We have a ready-to-use brochure structure that can help designers get a better idea of what we're looking for in the final brochure. We will also provide imagery, graphics, and copy that will be used in the brochure - designers will just have to piece them all together and add their own touch of flair to it!
We are looking for the design to clearly communicate what we we do from a product, service and system perspective. The design should inspire trust, be clear and concise, but also to incorporate the fun spirit that embodies our company and our mascots, Pemmo and Roddy.
Attached is a suggested brochure structure, previous brochures we have had designed, a project brief, as well as examples of what we like.
Company Name: Tidy Vault (operating under Bramwell Filing Group)
Company Location: Melbourne, Victoria, Australia
Contacts: niall@bramwellfilinggroup.com.au / desmond@bramwellfilinggroup.com.au
Project Type: 12-page A4 Brochure
Project Goal: A brochure that clearly communicates what we do from a product, service, and system perspective. The design should inspire trust, be clear and concise, but should also incorporate the fun spirit that embodies our company and our mascots, Pemmo and Roddi.
Final Output Format: .PDF and .AI or .INDD
Project Details and Scope of Work: We require a 14-page A4 brochure for our company based in Melbourne, VIC. Our company specializes in tailored archiving solutions for Australian schools of all sizes, and our main product is the "Tidy Vault" archiving system. We have a ready-to-use brochure structure that can help designers get a better idea of what we're looking for in the final brochure. We will also provide imagery, graphics, and copy that will be used in the brochure - designers will just have to piece them all together, fill in any gaps, and add their own touch of flair to it!
Links to Existing Content:
Graphics/Imagery*: https://files.example-share.net/folders/a7Kq2mT9xR4vLp8Wn3Zc
Brochure Copy:
https://files.example-share.net/docs/b3Hn8sV1yQ6tMd5Xk2Je
Photos:
https://files.example-share.net/folders/c9Pw4fL7uB2rNg6Ys1Dh
Previous Tidy Vault Brochures and Best Practice Design Examples Pages**:
https://files.example-share.net/folders/d5Tm3jR8oC1wKe7Vb4Fq
* Each folder, named after different sections of the brochure, contains graphics we would like to be used for that corresponding page/section.
** The photos in each folder are examples. Please refer to the Brochure Photo Folder for all options.
Target Market(s)
Schools of all sizes in Australia
Industry/Entity Type
Archiving / Storage
Look and feel

```html
<!DOCTYPE html>
<html lang="en">
<head>
<meta charset="utf-8">
<title>Tidy Vault – How It All Works</title>
<link href="https://fonts.googleapis.com/css2?family=Montserrat:wght@800&family=Oswald:wght@400;500;600&family=Open+Sans:wght@400;600&display=swap" rel="stylesheet">
<style>
  :root{
    --navy:#2c3850;
    --navy-deep:#232d42;
    --navy-mid:#37465f;
    --sky:#8fc8ea;
    --band:#3c6593;
    --band-dark:#2f557f;
    --orange:#f7a21b;
    --green:#8cc63e;
    --red:#e4232b;
    --white:#ffffff;
    --ink:#1e2638;
    --ghost:#353f56;
    --quote-ink:#1a2130;
    --attrib:#a6cbe6;
  }
  *{margin:0;padding:0;box-sizing:border-box}
  html,body{width:848px;height:1200px;overflow:hidden;background:var(--navy)}
  .page{position:relative;width:848px;height:1200px;overflow:hidden;background:var(--navy);font-family:"Open Sans",Arial,sans-serif}
  .backdrop,.process-map{position:absolute;left:0;top:0}
  .brand{position:absolute;right:22px;top:56px;display:flex;align-items:center;gap:10px;font-family:"Oswald",Arial,sans-serif;font-weight:600;font-size:34px;line-height:1;color:var(--white);letter-spacing:1px;text-transform:uppercase}
  .brand-mark{width:22px;height:22px;background:var(--white)}
  .headline{position:absolute;left:126px;top:96px;font-family:"Montserrat",Arial,sans-serif;font-weight:800;color:var(--white);font-size:64px;line-height:60px;letter-spacing:0}
  .step-label{position:absolute;font-family:"Oswald",Arial,sans-serif;font-weight:600;font-size:13.5px;letter-spacing:0;color:var(--green);text-transform:uppercase;line-height:1.1}
  .step-label.dark{color:var(--ink)}
  .step-label.light{color:var(--white)}
  .callout{position:absolute;background:var(--orange);color:var(--ink);font-size:9.5px;line-height:1.25;padding:6px 7px;box-shadow:4px 4px 0 var(--white)}
  .testimonial{position:absolute;left:0;top:1005px;width:848px;height:195px}
  .testimonial-ghost{position:absolute;left:22px;top:-12px;font-family:"Oswald",Arial,sans-serif;font-weight:600;font-size:150px;color:var(--ghost);line-height:1;letter-spacing:-2px}
  .quote-mark{position:absolute;font-family:"Montserrat",Arial,sans-serif;font-weight:800;font-size:170px;color:var(--quote-ink);line-height:1}
  .quote-mark.open{left:48px;top:-4px}
  .quote-mark.close{left:742px;top:70px}
  .quote-text{position:absolute;left:118px;top:48px;width:612px;text-align:center;font-family:"Oswald",Arial,sans-serif;font-weight:500;font-size:15.2px;line-height:1.42;color:var(--white);text-transform:uppercase}
  .attribution{position:absolute;right:120px;top:132px;text-align:right;font-family:"Oswald",Arial,sans-serif;color:var(--attrib)}
  .attribution .org{font-weight:600;font-size:15.5px;display:block}
  .attribution .person{font-weight:400;font-size:14.5px;display:block}
</style>
</head>
<body>
<main class="page">

  <svg class="backdrop" width="848" height="1200" viewBox="0 0 848 1200" aria-hidden="true">
    <defs>
      <linearGradient id="skyFade" x1="1" y1="0" x2="0" y2="1">
        <stop offset="0" stop-color="#a9d6f1"/>
        <stop offset="1" stop-color="#6fa9d4"/>
      </linearGradient>
    </defs>
    <rect width="848" height="1200" fill="var(--navy)"/>
    <polygon points="150,0 848,0 848,610 170,300" fill="url(#skyFade)"/>
    <polygon points="0,230 170,300 848,610 848,700 0,330" fill="var(--navy-mid)"/>
    <polygon points="0,0 150,0 170,300 0,230" fill="var(--navy-deep)"/>
    <polygon points="549,0 627,0 588,78" fill="var(--red)"/>
    <polygon points="48,92 672,92 660,218 110,218" fill="var(--band)"/>
    <polygon points="672,92 680,92 668,222 660,218" fill="var(--navy-deep)"/>
    <line x1="110" y1="222" x2="664" y2="222" stroke="var(--navy-deep)" stroke-width="4"/>
  </svg>

  <div class="brand"><span class="brand-mark"></span>Tidy Vault</div>
  <h1 class="headline">HOW IT<br>ALL WORKS</h1>

  <svg class="process-map" width="848" height="1200" viewBox="0 0 848 1200" aria-label="Process path from assessment to ongoing support">
    <path d="M150 627 H640 A73 73 0 0 1 640 773 H240" fill="none" stroke="var(--band)" stroke-width="66"/>
    <path d="M240 773 A70 70 0 0 0 240 913" fill="none" stroke="var(--orange)" stroke-width="66"/>
    <path d="M238 913 H790" fill="none" stroke="var(--band)" stroke-width="66"/>
    <polygon points="790,880 826,913 790,946" fill="var(--band)"/>
    <polygon points="12,594 170,594 204,627 170,660 12,660 46,627" fill="var(--orange)"/>
    <polygon points="300,594 326,594 360,627 326,660 300,660 334,627" fill="var(--band-dark)"/>
    <polygon points="574,740 548,740 514,773 548,806 574,806 540,773" fill="var(--band-dark)"/>

    <g fill="var(--ink)">
      <circle cx="66" cy="616" r="5"/><circle cx="77" cy="612" r="6"/><circle cx="88" cy="616" r="5"/>
      <rect x="60" y="623" width="12" height="22" rx="3"/><rect x="71" y="620" width="12" height="26" rx="3"/><rect x="82" y="623" width="12" height="22" rx="3"/>
    </g>
    <g fill="none" stroke="var(--white)" stroke-width="3.5">
      <circle cx="290" cy="622" r="9"/><line x1="284" y1="629" x2="276" y2="638"/>
    </g>
    <g fill="var(--sky)">
      <circle cx="370" cy="622" r="9"/><rect x="365" y="630" width="10" height="8"/>
      <line x1="370" y1="604" x2="370" y2="609" stroke="var(--sky)" stroke-width="2"/>
      <line x1="355" y1="622" x2="350" y2="622" stroke="var(--sky)" stroke-width="2"/>
      <line x1="385" y1="622" x2="390" y2="622" stroke="var(--sky)" stroke-width="2"/>
    </g>
    <g fill="var(--sky)">
      <ellipse cx="623" cy="615" rx="13" ry="4"/><rect x="610" y="618" width="26" height="6" rx="2"/><rect x="610" y="626" width="26" height="6" rx="2"/><rect x="610" y="634" width="26" height="6" rx="2"/>
    </g>
    <g fill="none" stroke="var(--sky)" stroke-width="3">
      <circle cx="285" cy="776" r="13"/><polyline points="285,768 285,777 292,780"/>
    </g>
    <path d="M485 776 L485 760 A16 16 0 1 1 469 776 Z" fill="var(--sky)"/>
    <path d="M479 774 A16 16 0 0 1 481 758 L481 774 Z" fill="var(--sky)"/>
    <g fill="var(--sky)"><polygon points="552,790 574,766 580,772 558,796 550,798"/></g>
    <g fill="var(--white)"><path d="M198 770 l10 -8 8 6 8 -6 10 8 -8 8 -6 -4 -6 4 z"/></g>
    <rect x="266" y="904" width="18" height="28" rx="3" fill="none" stroke="var(--sky)" stroke-width="3"/>
    <g fill="var(--sky)"><circle cx="342" cy="900" r="7"/><path d="M330 926 a12 12 0 0 1 24 0 z"/><rect x="350" y="886" width="14" height="9" rx="3" fill="var(--white)"/></g>
    <g fill="var(--sky)"><circle cx="548" cy="904" r="7"/><path d="M536 930 a12 12 0 0 1 24 0 z"/></g>

    <g>
      <path d="M122 582 L145 630 L168 582 Z" fill="var(--green)"/>
      <circle cx="145" cy="564" r="40" fill="var(--green)"/>
      <rect x="108" y="528" width="74" height="52" rx="6" fill="#a98f6e" role="img" aria-label="Illustration of stacked archive boxes with the mascot"/>
      <path d="M404 580 L427 627 L450 580 Z" fill="var(--green)"/>
      <circle cx="427" cy="563" r="40" fill="var(--green)"/>
      <rect x="400" y="522" width="54" height="62" rx="20" fill="#9b9b9b" role="img" aria-label="Illustration of the mascot giving a tailored solution"/>
      <path d="M602 736 L625 784 L648 736 Z" fill="var(--green)"/>
      <circle cx="625" cy="718" r="38" fill="var(--green)"/>
      <rect x="597" y="686" width="56" height="56" rx="8" fill="#b3433f" role="img" aria-label="Illustration of a worker moving archive boxes on a trolley"/>
      <path d="M397 752 L420 800 L443 752 Z" fill="var(--green)"/>
      <circle cx="420" cy="734" r="40" fill="var(--green)"/>
      <rect x="386" y="700" width="68" height="56" rx="8" fill="#7a6a58" role="img" aria-label="Illustration of a worker sorting records at a desk"/>
      <path d="M184 887 L207 935 L230 887 Z" fill="var(--green)"/>
      <circle cx="207" cy="869" r="40" fill="var(--green)"/>
      <rect x="172" y="840" width="70" height="48" rx="6" fill="#c0272d" role="img" aria-label="Illustration of the mascot beside installed shelving"/>
      <path d="M404 887 L427 935 L450 887 Z" fill="var(--green)"/>
      <circle cx="427" cy="869" r="40" fill="var(--green)"/>
      <rect x="392" y="840" width="70" height="50" rx="6" fill="#8a8f97" role="img" aria-label="Illustration of the mascot on a computer screen for software training"/>
      <path d="M753 880 L776 928 L799 880 Z" fill="var(--green)"/>
      <circle cx="776" cy="862" r="40" fill="var(--green)"/>
      <rect x="742" y="826" width="68" height="56" rx="6" fill="#5d5f66" role="img" aria-label="Illustration of a support person at a computer desk"/>
    </g>
  </svg>

  <div class="step-label dark" style="left:196px;top:619px">Assessment:</div>
  <div class="step-label" style="left:437px;top:619px">Quotation Acceptance:</div>
  <div class="step-label" style="left:668px;top:686px">Collection:</div>
  <div class="step-label" style="left:316px;top:768px">Processing:</div>
  <div class="step-label light" style="left:116px;top:790px">Installation:</div>
  <div class="step-label" style="left:458px;top:904px">Training:</div>
  <div class="step-label" style="left:614px;top:897px">Ongoing Support<br>&amp; Service:</div>

  <div class="callout" style="left:197px;top:527px;width:102px">Our experts assess school's archiving situation</div>
  <div class="callout" style="left:463px;top:532px;width:93px">Tailored solutions based on assessment</div>
  <div class="callout" style="left:738px;top:658px;width:95px">We collect and transport securely.</div>
  <div class="callout" style="left:268px;top:677px;width:95px">We sort, cull and index your records</div>
  <div class="callout" style="left:21px;top:841px;width:96px">Return records, build system, maximize space</div>
  <div class="callout" style="left:470px;top:815px;width:96px">Initial and ongoing software training provided.</div>
  <div class="callout" style="left:601px;top:815px;width:112px">Ongoing support when you need it, plus additional yearly archive services</div>

  <section class="testimonial">
    <div class="testimonial-ghost" aria-hidden="true">Testimonial</div>
    <div class="quote-mark open" aria-hidden="true">“</div>
    <div class="quote-mark close" aria-hidden="true">”</div>
    <p class="quote-text">The Tidy Vault team always offers great service, are always accessible and reliable when we have needed any assistance with products or the software. Whenever we have a query regarding our systems, they have always gotten back to me the same day.</p>
    <p class="attribution"><span class="org">Kelverton District High School</span><span class="person">Maree Holloway, Business Manager</span></p>
  </section>

</main>
</body>
</html>
```